Psychotherapy, Life Coaching, Writer, Motivational Speaker

I am a psychotherapist, life coach, writer and speaker on health and wellness issues. I am a humanist - who believes that we are born to self-actualize - but life - changes that course. That we develop armor and coping mechanisms that divert our growth. I help people examine their road blocks to happiness. My business is unique in that I do concierge therapy. I work intensively - with multi-day sessions, I work internationally through tele-therapy - and traditionally - in an office space. My work is tailored to your needs.

Target Market(s)

Broad

Industry/Entity Type

Health

Contact Information for Business Card

Listen To Grow
Sam Virelle
482 East 23rd Street
New York, NY 10027
(305) 418-7302

Requirements
Must have
• Clean lines... not too busy...
• FB page listing: Listen To Grow
• my Web page: www.listentogrow-example.com
Nice to have
• I would love to be able to list the services: Psychotherapist, Life Coach, Motivational Speaker and Writer - but also don't want a crazy crowded card. Feel free to use the back for description.
Should not have
• Stay away from corny imagery - lotus flowers, zen, lily pond, clouds.

```html
<!DOCTYPE html>
<html lang="en">
<head>
<meta charset="utf-8">
<title>Listen To Grow – Business Card</title>
<link rel="stylesheet" href="https://fonts.googleapis.com/css2?family=Source+Sans+3:wght@400;600;700&display=swap">
<style>
  :root {
    --stage: #c9cccc;
    --violet: #7b2fe0;
    --magenta: #e0258f;
    --crimson: #d9264c;
    --plum: #2b0a3d;
    --ink-panel: rgba(28, 12, 34, 0.88);
    --ring: #6a44f0;
    --ring-inner: #2a1530;
    --brand-tint: #a9eef0;
    --text-light: #ffffff;
    --bullet: #7a5cff;
    --portrait-a: #cfd8c8;
    --portrait-b: #8fa894;
  }
  * { box-sizing: border-box; margin: 0; padding: 0; }
  html, body {
    width: 1200px; height: 804px; overflow: hidden;
    background: var(--stage);
    font-family: "Source Sans 3", "Helvetica Neue", Arial, sans-serif;
  }
  .canvas { position: relative; width: 1200px; height: 804px; }

  .card { position: absolute; overflow: hidden; }
  .card--front { left: 84px; top: 38px; width: 432px; height: 723px; }
  .card--back  { left: 558px; top: 240px; width: 618px; height: 372px; }

  .facet-field {
    position: absolute; inset: 0;
    background:
      radial-gradient(ellipse 45% 30% at 20% 15%, var(--violet), transparent 70%),
      radial-gradient(ellipse 40% 30% at 80% 30%, var(--magenta), transparent 70%),
      radial-gradient(ellipse 50% 35% at 30% 55%, var(--crimson), transparent 70%),
      radial-gradient(ellipse 45% 35% at 75% 80%, var(--violet), transparent 70%),
      radial-gradient(ellipse 40% 30% at 20% 90%, var(--magenta), transparent 70%),
      linear-gradient(160deg, var(--plum), #8a1f6a 45%, var(--plum));
  }

  .portrait-ring {
    position: absolute; border-radius: 50%;
    background: var(--ring);
    display: flex; align-items: center; justify-content: center;
    z-index: 2;
  }
  .portrait-ring__inner {
    border-radius: 50%; background: var(--ring-inner);
    display: flex; align-items: center; justify-content: center;
  }
  .portrait {
    border-radius: 50%;
    background: radial-gradient(circle at 45% 40%, var(--portrait-a), var(--portrait-b));
  }

  .brand-bar {
    position: absolute; background: var(--ink-panel); border-radius: 4px;
    display: flex; align-items: center;
  }
  .brand-name {
    color: var(--brand-tint); font-weight: 400; letter-spacing: 0.2px;
    white-space: nowrap;
  }

  /* front */
  .card--front .portrait-ring { left: 126px; top: 54px; width: 164px; height: 164px; }
  .card--front .portrait-ring__inner { width: 140px; height: 140px; }
  .card--front .portrait { width: 116px; height: 116px; }
  .card--front .brand-bar { left: 55px; top: 256px; width: 323px; height: 82px; padding-left: 12px; }
  .card--front .brand-name { font-size: 27px; }

  .contact-panel {
    position: absolute; left: 55px; top: 422px; width: 323px; height: 235px;
    background: var(--ink-panel); border-radius: 4px;
    padding: 14px 0 0 20px; color: var(--text-light);
  }
  .contact-panel__title { font-size: 15px; font-weight: 700; margin-bottom: 11px; }
  .contact-list { list-style: none; }
  .contact-list__item {
    display: flex; align-items: center; height: 38px;
    font-size: 12.5px; white-space: nowrap;
  }
  .contact-list__bullet {
    width: 11px; height: 11px; border-radius: 50%;
    background: var(--text-light); border: 3px solid var(--bullet);
    margin-right: 14px; flex: none;
  }

  /* back */
  .card--back .portrait-ring { left: 55px; top: 107px; width: 158px; height: 158px; }
  .card--back .portrait-ring__inner { width: 136px; height: 136px; }
  .card--back .portrait { width: 114px; height: 114px; }
  .card--back .brand-bar { left: 137px; top: 142px; width: 419px; height: 94px; padding-left: 86px; }
  .card--back .brand-name { font-size: 30px; }
</style>
</head>
<body>
<main class="canvas">

  <section class="card card--front" aria-label="Card front">
    <div class="facet-field" role="img" aria-label="Faceted low-poly background in violet, magenta and crimson"></div>
    <div class="portrait-ring">
      <div class="portrait-ring__inner">
        <div class="portrait" role="img" aria-label="Portrait photo of Sam Virelle"></div>
      </div>
    </div>
    <div class="brand-bar"><span class="brand-name">Listen To Grow</span></div>
    <div class="contact-panel">
      <h2 class="contact-panel__title">contact info</h2>
      <ul class="contact-list">
        <li class="contact-list__item"><span class="contact-list__bullet"></span>Phone: (305) 418-7302</li>
        <li class="contact-list__item"><span class="contact-list__bullet"></span>Email: svirelle.studio@example.com</li>
        <li class="contact-list__item"><span class="contact-list__bullet"></span>Address: 482 East 23rd Street New York, NY 10027</li>
        <li class="contact-list__item"><span class="contact-list__bullet"></span>Social: Listen To Grow</li>
        <li class="contact-list__item"><span class="contact-list__bullet"></span>Web:&nbsp;&nbsp; www.listentogrow-example.com</li>
      </ul>
    </div>
  </section>

  <section class="card card--back" aria-label="Card back">
    <div class="facet-field" role="img" aria-label="Faceted low-poly background in violet, magenta and crimson"></div>
    <div class="brand-bar"><span class="brand-name">Listen To Grow</span></div>
    <div class="portrait-ring">
      <div class="portrait-ring__inner">
        <div class="portrait" role="img" aria-label="Portrait photo of Sam Virelle"></div>
      </div>
    </div>
  </section>

</main>
</body>
</html>
```